Business cards for Harbourline Supply Pty Ltd that import building products into Australia from China
Target Market(s)
Business to Business
Industry/Entity Type
Business
Contact Information for Business Card
Front: Logo and Business Name
Rear:
Vernon Asquill
General Manager
Mobile: 0427 196 354
email: vern@harbourlinesupply.com.au
alternative email: vern@ochrefield.com.au
web: www.harbourlinesupply.com.au
Adelaide, Brisbane and Darwin
Colors
ec1f27
fbee3d

```html
<!DOCTYPE html>
<html lang="en">
<head>
<meta charset="utf-8">
<title>Harbourline Supply – Business Cards</title>
<link rel="stylesheet" href="https://fonts.googleapis.com/css2?family=Arimo:wght@400&display=swap">
<style>
  :root {
    --brand-red: #ec1f27;
    --brand-yellow: #fbee3d;
    --card-yellow: #ffde00;
    --ghost-yellow: #fff03a;
    --backdrop: #3a2419;
    --white: #ffffff;
  }
  * { margin: 0; padding: 0; box-sizing: border-box; }
  html, body {
    width: 1200px; height: 448px; overflow: hidden;
    background: var(--backdrop);
    font-family: "Arimo", Arial, sans-serif;
  }
  .stage { position: relative; width: 1200px; height: 448px; }
  .card {
    position: absolute; top: 67px;
    width: 554px; height: 315px; overflow: hidden;
  }
  .card--contact { left: 32px; background: var(--brand-red); }
  .card--brand { left: 604px; background: var(--card-yellow); }

  .wordmark {
    position: absolute; font-weight: 400; letter-spacing: -0.02em;
    line-height: 0.95; white-space: nowrap;
  }
  .card--contact .wordmark {
    left: 28px; top: 118px; font-size: 33px; color: var(--brand-yellow);
  }
  .divider {
    position: absolute; left: 229px; top: 32px;
    width: 2px; height: 249px; background: var(--brand-yellow);
  }
  .person { position: absolute; left: 245px; top: 43px; }
  .person__name { font-size: 21px; color: var(--white); line-height: 1.2; }
  .person__role {
    font-size: 11.5px; color: var(--brand-yellow);
    text-transform: uppercase; margin-top: 3px; letter-spacing: 0.01em;
  }
  .contact-row {
    position: absolute; left: 248px;
    display: flex; align-items: flex-start; gap: 11px;
    color: var(--white); font-size: 16px; line-height: 22px;
  }
  .contact-row svg { width: 22px; height: 22px; flex: none; }
  .contact-row--phone { top: 139px; }
  .contact-row--email { top: 192px; }
  .contact-row--web { top: 257px; }

  .ghost-mark {
    position: absolute; left: 4px; top: 14px;
    font-size: 136px; line-height: 0.95; color: var(--ghost-yellow);
    white-space: nowrap; letter-spacing: -0.03em;
  }
  .card--brand .wordmark {
    left: 118px; top: 102px; font-size: 62px; color: var(--brand-red);
  }
</style>
</head>
<body>
<main class="stage">
  <section class="card card--contact" aria-label="Contact side">
    <div class="wordmark">harbourline<br>supply</div>
    <div class="divider"></div>
    <div class="person">
      <p class="person__name">Vernon Asquill</p>
      <p class="person__role">General Manager</p>
    </div>
    <div class="contact-row contact-row--phone">
      <svg viewBox="0 0 22 22" aria-hidden="true">
        <circle cx="11" cy="11" r="11" fill="var(--brand-yellow)"/>
        <rect x="7.5" y="4.5" width="7" height="13" rx="1.3" fill="var(--brand-red)"/>
        <rect x="8.7" y="6" width="4.6" height="8.8" fill="var(--brand-yellow)"/>
      </svg>
      <span>0427 196 354</span>
    </div>
    <div class="contact-row contact-row--email">
      <svg viewBox="0 0 22 22" aria-hidden="true">
        <circle cx="11" cy="11" r="11" fill="var(--brand-yellow)"/>
        <rect x="5.5" y="7" width="11" height="8" rx="1" fill="var(--brand-red)"/>
        <path d="M5.8 7.5 L11 11.5 L16.2 7.5" fill="none" stroke="var(--brand-yellow)" stroke-width="1.1"/>
      </svg>
      <span>vern@harbourlinesupply.com.au<br>vern@ochrefield.com.au</span>
    </div>
    <div class="contact-row contact-row--web">
      <svg viewBox="0 0 22 22" aria-hidden="true">
        <circle cx="11" cy="11" r="11" fill="var(--brand-yellow)"/>
        <g fill="none" stroke="var(--brand-red)" stroke-width="1.1">
          <circle cx="11" cy="11" r="5.5"/>
          <ellipse cx="11" cy="11" rx="2.4" ry="5.5"/>
          <path d="M5.5 11 H16.5 M6.3 8.2 H15.7 M6.3 13.8 H15.7"/>
        </g>
      </svg>
      <span>0427 196 354</span>
    </div>
  </section>

  <section class="card card--brand" aria-label="Brand side">
    <div class="ghost-mark" aria-hidden="true">harbourline<br>supply</div>
    <div class="wordmark">harbourline<br>supply</div>
  </section>
</main>
</body>
</html>
```